Stylish Business Cards Wanted

- DOUBLE SIDED Design Required -

High end, edgy cards for a corporate and personal stylist. Must include logo,
Name: Belinda Forsey
Title: Director and Stylist
telephone : +61 8 8217 4592
email: belinda@thegarbledger.example
website: thegarbledger.example
Tag: Corporate Workwear & Uniform Specialist | Personal Stylist
Would like nice icons for telephone, email, website

Target Market(s)

Businesses wanting stylish uniforms, people wanting stylish wardrobes

Industry/Entity Type

Corporate Workwear Stylist

Contact Information for Business Card

I would like black, white and gold foiling incorporated in the design - possibly a touch of the other colours on my branding guide attached Name: Belinda Forsey Title: Director and Stylist telephone : +61 8 8217 4592 email: belinda@thegarbledger.example website: thegarbledger.example Tag: Corporate Workwear & Uniform Specialist | Personal Stylist Would like nice icons for telephone, email, website

Font styles to use
Other font styles liked:
• Raleway

Colors

Designer to choose colors to be used in the design.

Requirements
Must have
• Gold foil accents

```html
<!DOCTYPE html>
<html lang="en">
<head>
<meta charset="utf-8">
<title>The Garb Ledger – Business Cards</title>
<link href="https://fonts.googleapis.com/css2?family=Raleway:wght@500;600;700&display=swap" rel="stylesheet">
<style>
  :root {
    --backdrop: #f7921e;
    --band-orange: #f7921e;
    --gold: #f9ae3b;
    --ink: #000000;
    --paper: #ffffff;
    --text-dark: #111111;
  }
  html, body {
    margin: 0;
    padding: 0;
    width: 1200px;
    height: 1200px;
    overflow: hidden;
    background: var(--backdrop);
  }
  .canvas {
    position: relative;
    width: 1200px;
    height: 1200px;
  }
  .card {
    position: absolute;
    left: 253px;
    width: 692px;
    height: 366px;
    display: block;
  }
  .card--front { top: 215px; }
  .card--back { top: 619px; }
  .card text {
    font-family: "Raleway", sans-serif;
  }
  .brand-name { font-weight: 700; fill: var(--text-dark); }
  .holder-name { font-weight: 700; font-size: 48px; fill: var(--ink); }
  .holder-title { font-weight: 600; font-size: 14px; letter-spacing: 11px; fill: var(--ink); }
  .tagline { font-weight: 600; font-size: 15px; fill: var(--ink); }
  .contact-line { font-weight: 700; font-size: 30px; fill: var(--ink); }
  .icon-line { fill: none; stroke: var(--ink); stroke-width: 3; }
</style>
</head>
<body>
<main class="canvas">

  <!-- Front of card -->
  <svg class="card card--front" viewBox="0 0 1113 588" role="group" aria-label="Business card front">
    <rect class="card-paper" x="0" y="0" width="1113" height="588" fill="var(--paper)"/>
    <polygon class="ink-panel" points="0,0 419,0 370,36 370,552 419,588 0,588" fill="var(--ink)"/>
    <polyline class="gold-frame" points="379,36 189,36 38,293 189,552 379,552" fill="none" stroke="var(--gold)" stroke-width="9"/>
    <polygon class="logo-hexagon" points="64,293 196,50 479,50 620,293 479,536 196,536" fill="var(--paper)" stroke="var(--ink)" stroke-width="11"/>
    <polygon class="name-band" points="580,191 1113,191 1113,398 580,398 640,293" fill="var(--band-orange)"/>

    <g class="brand-lockup">
      <text class="brand-name" x="342" y="280" font-size="30" text-anchor="middle" letter-spacing="6">THE</text>
      <text class="brand-name" x="342" y="340" font-size="62" text-anchor="middle">Garb Ledger</text>
    </g>

    <text class="holder-name" x="674" y="297">BELINDA FORSEY</text>
    <text class="holder-title" x="674" y="319">DIRECTOR AND STYLIST</text>
    <text class="tagline" x="575" y="428">CORPORATE WORKWEAR | UNIFORM SPECIALIST | PERSONAL STYLIST</text>
  </svg>

  <!-- Back of card -->
  <svg class="card card--back" viewBox="0 0 1113 588" role="group" aria-label="Business card back">
    <rect class="card-paper" x="0" y="0" width="1113" height="588" fill="var(--paper)"/>
    <rect class="ink-stripe" x="0" y="130" width="1113" height="118" fill="var(--ink)"/>
    <polygon class="hexagon-gap" points="425,188 496,74 628,74 699,188 628,302 496,302" fill="var(--paper)"/>
    <polygon class="logo-hexagon" points="437,188 503,83 621,83 687,188 621,291 503,291" fill="var(--paper)" stroke="var(--gold)" stroke-width="4"/>
    <g class="brand-lockup">
      <text class="brand-name" x="562" y="177" font-size="15" text-anchor="middle" letter-spacing="3">THE</text>
      <text class="brand-name" x="562" y="208" font-size="30" text-anchor="middle">Garb Ledger</text>
    </g>

    <rect class="contact-band" x="0" y="405" width="1113" height="183" fill="var(--band-orange)"/>

    <g class="contact contact--phone">
      <circle class="icon-line" cx="94" cy="449" r="17"/>
      <path class="icon-line" d="M86,440 q-3,4 2,12 q5,8 12,8 l3,-4 l-5,-4 l-3,3 q-5,-3 -7,-8 l3,-2 l-3,-6 z" stroke-width="2.5"/>
      <text class="contact-line" x="118" y="460">+61 8 8217 4592</text>
    </g>
    <g class="contact contact--web">
      <circle class="icon-line" cx="96" cy="495" r="17"/>
      <circle class="icon-line" cx="96" cy="495" r="11" stroke-width="2"/>
      <ellipse class="icon-line" cx="96" cy="495" rx="5" ry="11" stroke-width="2"/>
      <path class="icon-line" d="M85,495 h22 M87,489 h18 M87,501 h18" stroke-width="2"/>
      <text class="contact-line" x="122" y="506">thegarbledger.example</text>
    </g>
    <g class="contact contact--email">
      <circle class="icon-line" cx="94" cy="541" r="17"/>
      <rect class="icon-line" x="84" y="534" width="20" height="14" stroke-width="2.5"/>
      <path class="icon-line" d="M84,534 l10,8 l10,-8" stroke-width="2.5"/>
      <text class="contact-line" x="119" y="552">belinda@thegarbledger.example</text>
    </g>
  </svg>

</main>
</body>
</html>
```